Quiet Harbor Hours Podcast Artwork

I need a cover for my podcast Quiet Harbor Hours that is clean, modern, and minimalist, but not too feminine

Target Market(s)

People struggling with fertility particularly women who are between the ages of 35-45 though there is a small set of listeners who are men

Requirements
Must have
• Anchor in the Calm
Should not have
• No script text

```html
<!DOCTYPE html>
<html lang="en">
<head>
<meta charset="utf-8">
<title>Quiet Harbor Hours — Podcast Cover</title>
<link rel="stylesheet" href="https://fonts.googleapis.com/css2?family=Alegreya:wght@700&family=Alegreya+Sans:wght@600&display=swap">
<style>
  :root {
    --page-bg: #efefef;
    --cover-bg: #fdf6ea;
    --show-name: #8d4f3a;
    --title: #cc6e45;
    --mark: #8d503a;
  }
  * { margin: 0; padding: 0; box-sizing: border-box; }
  html, body {
    width: 900px;
    height: 1200px;
    overflow: hidden;
    background: var(--page-bg);
  }
  .cover {
    position: absolute;
    left: 0;
    top: 150px;
    width: 900px;
    height: 900px;
    background: var(--cover-bg);
  }
  .show-name {
    position: absolute;
    top: 198px;
    width: 100%;
    text-align: center;
    font-family: "Alegreya Sans", sans-serif;
    font-weight: 600;
    font-size: 36px;
    line-height: 44px;
    letter-spacing: 0.2px;
    color: var(--show-name);
  }
  .mark-area {
    position: absolute;
    left: 304px;
    top: 303px;
    width: 292px;
    height: 226px;
    border-radius: 18px;
    background: linear-gradient(180deg, #a56a52 0%, var(--mark) 100%);
    opacity: 0.85;
  }
  .episode-title {
    position: absolute;
    top: 556px;
    width: 100%;
    text-align: center;
    font-family: "Alegreya", serif;
    font-weight: 700;
    font-size: 52px;
    line-height: 59px;
    letter-spacing: 3px;
    color: var(--title);
  }
</style>
</head>
<body>
  <main class="cover">
    <p class="show-name">Quiet Harbor Hours</p>
    <div class="mark-area" role="img" aria-label="Podcast microphone emblem flanked by heartbeat lines"></div>
    <h1 class="episode-title">ANCHOR IN THE<br>CALM</h1>
  </main>
</body>
</html>
```